Business cards for a plastic surgeon's practice

We need some creative business cards designs for a plastic surgeon's practice. I'm attaching our logos ([login to view URL] and [login to view URL]). You can use combinations of the two or just the text. All the files (.psd and .ai files formats) are attached to the project.

IMPORTANT: Don't use the whole .psd files as I've uploaded them - each of them contains different sizes of the HAND and TEXT graphics. Just use one of the sizes on the .psd files.

REQUIREMENTS:
- Use the TEXT graphic or a combination of the TEXT and HAND graphics.
- Clear design, using light color in a combination of tiffany blue (#0abab5) or a similar color combination.
- ADDITIONAL POINTS FOR CREATIVITY. We want to be different and original, so we are open to ideas such as transparent business cards or non-rectangular shaped business cards.
- Include "Plastic Surgery" underneath "VORNIX", as well as our slogan, which is "Get the body and confidence you deserve".
- Include a placeholder for a name, phone number, website, physical address and email address.
- We need a two-sided business card, so be creative about the content on the back of the business card.

If we're happy with a business card design we receive, we might pay additionally for tweaks and assistance with putting it to use.

Benedikt

```html
<!DOCTYPE html>
<html lang="en">
<head>
<meta charset="utf-8">
<title>VORNIX Plastic Surgery – Business Cards</title>
<link rel="stylesheet" href="https://fonts.googleapis.com/css2?family=Lato:wght@300;400;700;900&display=swap">
<style>
  :root {
    --brand-teal: #0abab5;
    --card-white: #ffffff;
    --ink: #1c1c1c;
    --ink-soft: #3a3a3a;
    --backdrop: #dcdcdc;
    --hand-light: #c9ccd3;
    --hand-mid: #8e95a3;
    --hand-dark: #4f5a72;
  }
  * { box-sizing: border-box; margin: 0; padding: 0; }
  html, body {
    width: 1200px; height: 900px; overflow: hidden;
    background: var(--backdrop);
    font-family: "Lato", sans-serif;
  }
  .sheet { position: relative; width: 1200px; height: 900px; }

  .card { position: absolute; width: 540px; height: 310px; }
  .card__shape { position: absolute; inset: 0; width: 540px; height: 310px; }

  .card--front { left: 600px; top: 110px; }
  .card--back  { left: 60px;  top: 480px; }

  .front-brand {
    position: absolute; right: 40px; top: 62px;
    text-align: right; color: var(--card-white);
  }
  .front-brand__name {
    font-weight: 700; font-size: 64px; letter-spacing: 1px; line-height: 1;
  }
  .front-brand__service {
    font-weight: 700; font-size: 28px; margin-top: 12px;
  }
  .front-brand__slogan {
    font-weight: 400; font-size: 14px; margin-top: 10px; letter-spacing: .2px;
  }

  .back-identity { position: absolute; left: 40px; top: 150px; }
  .back-identity__name {
    font-weight: 900; font-size: 24px; color: var(--ink); letter-spacing: .5px;
  }
  .back-identity__role {
    font-weight: 400; font-size: 15px; color: var(--ink-soft); margin-top: 2px;
  }
  .contact-list { list-style: none; margin-top: 18px; }
  .contact-list__item {
    display: flex; align-items: center; gap: 10px;
    font-size: 13px; color: var(--ink-soft); height: 20px;
  }
  .contact-list__icon { width: 13px; height: 13px; flex: none; }
</style>
</head>
<body>
<main class="sheet">

  <!-- Front side -->
  <section class="card card--front">
    <svg class="card__shape" viewBox="0 0 540 310" aria-hidden="true">
      <defs>
        <linearGradient id="handToneFront" x1="0" y1="0" x2="1" y2="1">
          <stop offset="0" stop-color="var(--hand-light)"/>
          <stop offset=".55" stop-color="var(--hand-mid)"/>
          <stop offset="1" stop-color="var(--hand-dark)"/>
        </linearGradient>
      </defs>
      <path d="M90 0 H510 Q540 0 540 30 V280 Q540 310 510 310 H230 L170 140 Z" fill="var(--brand-teal)"/>
    </svg>
    <svg class="card__shape" viewBox="0 0 540 310" role="img" aria-label="Illustration of an open hand reaching in from the left">
      <path d="M0 150 Q40 130 100 140 Q170 150 220 190 Q270 230 275 265 Q278 290 250 300 L230 310 H40 Q14 310 10 288 L4 250 Q0 230 8 210 L2 180 Q-2 160 6 150 Z" fill="url(#handToneFront)"/>
    </svg>
    <div class="front-brand">
      <div class="front-brand__name">VORNIX</div>
      <div class="front-brand__service">Plastic Surgery</div>
      <div class="front-brand__slogan">Get the body and confidence you deserve</div>
    </div>
  </section>

  <!-- Back side -->
  <section class="card card--back">
    <svg class="card__shape" viewBox="0 0 540 310" aria-hidden="true">
      <path d="M28 40 H380 V310 H28 Q0 310 0 282 V68 Q0 40 28 40 Z" fill="var(--card-white)"/>
    </svg>
    <svg class="card__shape" viewBox="0 0 540 310" role="img" aria-label="Illustration of an open hand reaching down from the top right">
      <defs>
        <linearGradient id="handToneBack" x1="1" y1="0" x2="0" y2="1">
          <stop offset="0" stop-color="var(--hand-light)"/>
          <stop offset=".5" stop-color="var(--hand-mid)"/>
          <stop offset="1" stop-color="var(--hand-dark)"/>
        </linearGradient>
      </defs>
      <path d="M240 40 Q300 10 380 0 H512 Q540 0 540 28 V120 Q530 150 538 180 Q520 210 528 240 Q500 290 440 306 L380 310 Q330 290 320 240 Q312 190 330 140 Q300 100 240 40 Z" fill="url(#handToneBack)"/>
    </svg>
    <div class="back-identity">
      <div class="back-identity__name">DANIEL HARPER</div>
      <div class="back-identity__role">Plastic Surgion</div>
      <ul class="contact-list">
        <li class="contact-list__item">
          <svg class="contact-list__icon" viewBox="0 0 16 16"><path d="M4 1 L6 5 L4.5 6.5 Q6 10 9.5 11.5 L11 10 L15 12 L14 15 Q6 15 1 5 Z" fill="none" stroke="var(--brand-teal)" stroke-width="1.4" stroke-linejoin="round"/></svg>
          <span>+10 555 201 384</span>
        </li>
        <li class="contact-list__item">
          <svg class="contact-list__icon" viewBox="0 0 16 16"><rect x="1.5" y="3.5" width="13" height="9" rx="1" fill="none" stroke="var(--brand-teal)" stroke-width="1.4"/><path d="M1.5 4 L8 9 L14.5 4" fill="none" stroke="var(--brand-teal)" stroke-width="1.4"/></svg>
          <span>hello@vornixclinic.com</span>
        </li>
        <li class="contact-list__item">
          <svg class="contact-list__icon" viewBox="0 0 16 16"><circle cx="8" cy="8" r="6.5" fill="none" stroke="var(--brand-teal)" stroke-width="1.4"/><ellipse cx="8" cy="8" rx="2.8" ry="6.5" fill="none" stroke="var(--brand-teal)" stroke-width="1.2"/><path d="M1.5 8 H14.5" stroke="var(--brand-teal)" stroke-width="1.2"/></svg>
          <span>www.vornixclinic.com</span>
        </li>
        <li class="contact-list__item">
          <svg class="contact-list__icon" viewBox="0 0 16 16"><path d="M8 15 Q2.5 9 2.5 6 A5.5 5.5 0 0 1 13.5 6 Q13.5 9 8 15 Z" fill="none" stroke="var(--brand-teal)" stroke-width="1.4"/><circle cx="8" cy="6" r="2" fill="var(--brand-teal)"/></svg>
          <span>your address</span>
        </li>
      </ul>
    </div>
  </section>

</main>
</body>
</html>
```